Stationary and Business Card Design

We need a stationery design and a business card design for a non-profit economics development agency. Our website is brightledgerhub.org. Our clients are Canadian government agencies and large Chinese company. We need the design to be professional and corporate.

Please see attached for our Power Point presentation. Please take design elements from our website and our ppt.

```html
<!DOCTYPE html>
<html lang="en">
<head>
<meta charset="utf-8">
<title>Bright Ledger Hub – Stationery Set</title>
<link href="https://fonts.googleapis.com/css2?family=Arimo:wght@400;700&display=swap" rel="stylesheet">
<style>
:root{
  --red:#ff0019;
  --white:#ffffff;
  --ink:#1a1a1a;
  --stage:#8e8e8e;
  --faint-on-red:rgba(255,255,255,.09);
  --faint-on-white:rgba(0,0,0,.05);
  --shadow:3px 4px 8px rgba(0,0,0,.45);
}
*{box-sizing:border-box;margin:0;padding:0}
html,body{width:779px;height:1200px;overflow:hidden}
body{background:radial-gradient(ellipse at center,#a3a3a3 0%,var(--stage) 70%,#7d7d7d 100%);font-family:"Arimo",Arial,sans-serif;color:var(--ink);position:relative}
.piece{position:absolute;background:var(--white);box-shadow:var(--shadow);overflow:hidden}
.piece--red{background:var(--red)}

/* brand mark: invented name + one plain square */
.brand{position:absolute;display:flex;align-items:center;gap:4px;font-weight:700;color:var(--red);white-space:nowrap}
.brand__square{display:inline-block;background:currentColor}
.brand--white{color:var(--white)}
.brand--grey{color:rgba(0,0,0,.12)}

.faint-mark{position:absolute;font-weight:700;line-height:.85;white-space:nowrap}
.faint-mark--on-red{color:var(--faint-on-red)}
.faint-mark--on-white{color:var(--faint-on-white)}

.contact{position:absolute;font-size:6px;line-height:1.2;color:var(--ink);white-space:nowrap}
.contact .web{color:var(--red)}
.contact--right{text-align:right}
.contact--center{text-align:center}

.social{position:absolute;display:flex;gap:2px}
.social span{display:block;background:var(--red)}

/* items */
.letter-back{left:78px;top:17px;width:297px;height:386px}
.letter-front{left:390px;top:17px;width:296px;height:386px}
.card-vertical{left:586px;top:351px;width:149px;height:236px;z-index:2}
.card-front{left:74px;top:440px;width:235px;height:147px}
.card-front__panel{position:absolute;left:0;top:0;width:107px;height:100%;background:var(--red)}
.card-back{left:329px;top:440px;width:237px;height:147px}
.envelope-window{left:28px;top:613px;width:344px;height:152px}
.envelope-window__window{position:absolute;left:29px;top:80px;width:133px;height:47px;background:var(--red);border-radius:5px;box-shadow:inset 0 0 4px rgba(0,0,0,.35)}
.envelope-flap{left:393px;top:613px;width:344px;height:152px}
.envelope-flap__flap{position:absolute;left:0;top:0;width:100%;height:45px;background:var(--red);border-radius:0 0 14px 14px;box-shadow:0 3px 5px rgba(0,0,0,.3)}
.letter-plain{left:81px;top:797px;width:294px;height:386px}
.comp-slip{left:394px;top:797px;width:343px;height:151px}
.envelope-plain{left:394px;top:973px;width:343px;height:151px}
.envelope-plain__flap{position:absolute;left:0;top:0;width:100%;height:48px;border-radius:0 0 14px 14px;box-shadow:0 3px 5px rgba(0,0,0,.22);background:var(--white)}
.footer-line{position:absolute;left:8px;right:8px;bottom:11px;display:flex;justify-content:space-between;gap:5px;font-size:4.2px;white-space:nowrap;color:var(--ink)}
.card-name{position:absolute;left:0;right:0;top:84px;text-align:center;font-size:9px}
</style>
</head>
<body>

<!-- red letterhead reverse -->
<section class="piece piece--red letter-back" aria-label="Letterhead reverse">
  <div class="brand brand--white" style="right:8px;top:10px;font-size:10px"><span class="brand__square" style="width:9px;height:9px"></span>Bright Ledger Hub</div>
  <div class="faint-mark faint-mark--on-red" style="left:0;top:390px;font-size:150px;transform:rotate(-90deg);transform-origin:left top">BLH</div>
</section>

<!-- white letterhead -->
<section class="piece letter-front" aria-label="Letterhead">
  <div class="contact" style="left:13px;top:13px;font-size:5px;line-height:1.15">2750 Harbour Rd. West, Suite 412<br>Oakridge, Ontario, K7P 2M5<br>Phone: 555 014 7720<br>info@brightledgerhub.org<br>brightledgerhub.org</div>
  <div class="social" style="left:13px;top:45px"><span style="width:6px;height:6px"></span><span style="width:6px;height:6px"></span><span style="width:6px;height:6px"></span><span style="width:6px;height:6px"></span></div>
  <div class="brand" style="right:12px;top:18px;font-size:9px"><span class="brand__square" style="width:8px;height:8px"></span>Bright Ledger Hub</div>
  <div class="faint-mark faint-mark--on-white" style="left:5px;top:382px;font-size:80px;transform:rotate(-90deg);transform-origin:left top">BLH</div>
</section>

<!-- vertical business card -->
<section class="piece card-vertical" aria-label="Business card, portrait">
  <div class="brand" style="left:0;right:0;justify-content:center;top:18px;font-size:8px"><span class="brand__square" style="width:7px;height:7px"></span>Bright Ledger Hub</div>
  <div class="card-name">Name Surname</div>
  <div class="contact contact--center" style="left:0;right:0;top:120px;font-size:7px">2750 Harbour Rd. West, Suite 412<br>Oakridge, Ontario, K7P 2M5<br>Phone: 555 014 7720<br>info@brightledgerhub.org</div>
  <div class="contact contact--center" style="left:0;right:0;top:196px;font-size:8px"><span class="web">brightledgerhub.org</span></div>
  <div class="social" style="left:46px;top:209px"><span style="width:13px;height:13px"></span><span style="width:13px;height:13px"></span><span style="width:13px;height:13px"></span><span style="width:13px;height:13px"></span></div>
</section>

<!-- business card front -->
<section class="piece card-front" aria-label="Business card, landscape">
  <div class="card-front__panel"></div>
  <div class="brand brand--white" style="left:8px;top:56px;font-size:7px"><span class="brand__square" style="width:8px;height:8px"></span>Bright Ledger Hub</div>
  <div class="contact contact--right" style="right:5px;top:10px;font-size:7px">2750 Harbour Rd. West, Suite 412<br>Oakridge, Ontario, K7P 2M5<br>Phone: 555 014 7720<br>info@brightledgerhub.org<br><span class="web">brightledgerhub.org</span></div>
  <div class="social" style="right:7px;top:126px"><span style="width:11px;height:11px"></span><span style="width:11px;height:11px"></span><span style="width:11px;height:11px"></span><span style="width:11px;height:11px"></span></div>
</section>

<!-- business card back -->
<section class="piece piece--red card-back" aria-label="Business card reverse">
  <div class="faint-mark faint-mark--on-red" style="left:12px;top:142px;font-size:64px;transform:rotate(-90deg);transform-origin:left top">BLH</div>
</section>

<!-- window envelope -->
<section class="piece envelope-window" aria-label="Window envelope">
  <div class="contact" style="left:189px;top:6px;font-size:5.5px">2750 Harbour Rd. West, Suite 412<br>Oakridge, Ontario, K7P 2M5</div>
  <div class="contact contact--right" style="right:6px;top:6px;font-size:5.5px">Phone: 555 014 7720<br>info@brightledgerhub.org<br><span class="web">brightledgerhub.org</span></div>
  <div class="brand" style="left:46px;top:42px;font-size:10px"><span class="brand__square" style="width:10px;height:10px"></span>Bright Ledger Hub</div>
  <div class="envelope-window__window"></div>
</section>

<!-- envelope with red flap -->
<section class="piece envelope-flap" aria-label="Envelope with flap">
  <div class="envelope-flap__flap"></div>
  <div class="brand brand--white" style="left:17px;top:13px;font-size:7px"><span class="brand__square" style="width:7px;height:7px"></span>Bright Ledger Hub</div>
</section>

<!-- plain letterhead -->
<section class="piece letter-plain" aria-label="Letterhead, footer version">
  <div class="brand" style="left:0;right:0;justify-content:center;top:22px;font-size:9px"><span class="brand__square" style="width:8px;height:8px"></span>Bright Ledger Hub</div>
  <div class="faint-mark faint-mark--on-white" style="left:95px;top:320px;font-size:44px">BLH</div>
  <div class="footer-line"><span>2750 Harbour Rd. West, Suite 412</span><span>Oakridge, Ontario, K7P 2M5</span><span>Phone: 555 014 7720</span><span>info@brightledgerhub.org</span><span>brightledgerhub.org</span></div>
</section>

<!-- compliment slip -->
<section class="piece comp-slip" aria-label="Compliment slip">
  <div class="brand" style="left:7px;top:8px;font-size:7px"><span class="brand__square" style="width:7px;height:7px"></span>Bright Ledger Hub</div>
  <div class="contact" style="left:8px;top:111px;font-size:5.5px">2750 Harbour Rd. West, Suite 412<br>Oakridge, Ontario, K7P 2M5<br>Phone: 555 014 7720<br>info@brightledgerhub.org<br>brightledgerhub.org</div>
  <div class="faint-mark faint-mark--on-white" style="left:282px;top:150px;font-size:60px;transform:rotate(-90deg);transform-origin:left top">BLH</div>
</section>

<!-- plain envelope -->
<section class="piece envelope-plain" aria-label="Envelope, plain">
  <div class="envelope-plain__flap"></div>
  <div class="brand brand--grey" style="right:6px;top:110px;font-size:8px"><span class="brand__square" style="width:8px;height:8px"></span>Bright Ledger Hub</div>
</section>

</body>
</html>
```